FoldKite App for On-Demand Laundry

We are launching a startup of online laundry service using mobile app. This startup will give the most convenient experience for the customers in managing their laundry. In only few taps away with the app, we'll send our agents to pick up laundry at the customer's doorstep, proceed it as per their order type, and get it delivered back to them in a schedule that fits them well.

We need somebody that can help with us and make our app as one of the simplest yet most effective app to use, design should be clean and easy to navigate, leave experience that makes our users want to come back and use it again. It will consist of key features that the app should have as follows:

- Sign up & Login
- Add customer address
- Schedule laundry pick up & delivery
- Laundry service selection
- Confirmation and Payment
- Status Tracking

Please refer to the attachment for details of business flows. Example of apps that can inspire: Rinsely, Sudzoria, Presqo.

--PLEASE DO NOT USE THE LOGO FROM ATTACHMENT, IT'S ONLY A DUMMY LOGO--
Updates

Target Market(s)

Young Professional, College Students, Young Early Family

Industry/Entity Type

Cleaning Service

Font styles to use
Sans Serif

Colors
ffffff
9d9d9d
0392cd
33a6d7
86cfc6
33b8a4
acd036
cadf82

Requirements
Must have
• Simplicity and elegance. Clean and easy navigation.
• Example from attachment is "ugly" but can tell the overall idea on what information to capture from the app. We need to get a completely different design which is way better than it.
Nice to have
• Inspiration could be from similar apps like: Rinsely, Sudzoria, and Presqo.
Should not have
• --PLEASE DO NOT USE THE LOGO FROM ATTACHMENT, IT'S ONLY A DUMMY LOGO--

```html
<!DOCTYPE html>
<html lang="en">
<head>
<meta charset="utf-8">
<title>FoldKite — App Screens</title>
<link rel="stylesheet" href="https://fonts.googleapis.com/css2?family=Roboto:wght@300;400;500;700&family=Source+Serif+4:wght@300;400&display=swap">
<style>
:root{
  --navy:#2f4e6b;
  --navy-light:#3a5c7b;
  --navy-dark:#2a465f;
  --green:#a8c93a;
  --green-soft:#cadf82;
  --ink:#3b4652;
  --muted:#9d9d9d;
  --line:#d7dadd;
  --paper:#f4f5f6;
  --page:#ffffff;
}
*{box-sizing:border-box;margin:0;padding:0}
html,body{width:1200px;height:1200px;overflow:hidden;background:var(--page)}
body{position:relative;font-family:"Roboto",sans-serif;color:var(--ink)}
.deck-title{position:absolute;left:64px;top:484px;transform:translate(-50%,-50%) rotate(-90deg);white-space:nowrap;font-size:33px;font-weight:300;color:#3a5f82;letter-spacing:.5px}
.deck-title b{font-weight:700}
.screen{position:absolute;width:253px;height:450px;background:var(--paper);overflow:hidden;box-shadow:0 6px 18px rgba(0,0,0,.12)}
.abs{position:absolute;left:0;width:100%;text-align:center}
.serif{font-family:"Source Serif 4",serif;font-weight:300}
.hdr{font-size:12px;color:var(--ink)}
.hdr .lead{font-family:"Source Serif 4",serif;color:var(--green);font-weight:400}
.icon-btn{position:absolute;left:50%;transform:translateX(-50%)}
.step{position:absolute;width:13px;height:13px;border-radius:50%;background:var(--green);color:#fff;font-size:8px;font-weight:500;text-align:center;line-height:13px}
.field-label{position:absolute;left:34px;font-family:"Source Serif 4",serif;font-size:10px;color:var(--muted)}
.rule{position:absolute;left:34px;right:34px;height:1px;background:var(--line)}
.tag{position:absolute;font-size:7px;font-weight:500;color:var(--green);letter-spacing:.3px}
.val{position:absolute;font-size:11.5px;color:var(--ink)}
.arrow{position:absolute;font-size:10px;color:var(--green)}
.bar{position:absolute;left:0;bottom:0;width:100%;height:41px;background:var(--navy);color:#fff;font-size:8px;font-weight:500;text-align:center;line-height:41px;letter-spacing:.4px}
.total-label{position:absolute;right:34px;font-size:7.5px;font-weight:500;color:var(--ink)}
.total{position:absolute;right:34px;font-family:"Source Serif 4",serif;font-weight:300;font-size:23px;color:var(--green)}
/* login */
.login-bg{position:absolute;inset:0;background:linear-gradient(160deg,#466a8c 0%,#355676 50%,#2c4864 100%)}
.brand{position:absolute;top:58px;left:0;width:100%;text-align:center;font-size:20px;font-weight:300;color:#fff;letter-spacing:1px}
.login-copy{color:#e9eef3;font-size:11.5px;font-weight:300;line-height:15px}
.login-field{position:absolute;left:43px;right:41px;height:1px;background:rgba(255,255,255,.35)}
.login-btn{position:absolute;left:43px;top:278px;width:173px;height:28px;background:var(--green);color:#fff;font-size:7.5px;font-weight:500;text-align:center;line-height:28px}
/* home */
.home-top{position:absolute;left:0;top:0;width:100%;height:236px;background:var(--paper)}
.avatar{position:absolute;left:106px;top:68px;width:40px;height:40px;border-radius:50%;background:radial-gradient(circle at 50% 40%,#e9c6b4,#c79a86)}
.greet{font-size:11px;color:var(--ink)}
.greet .name{font-family:"Source Serif 4",serif;color:var(--green)}
.new-order{position:absolute;left:75px;top:185px;width:102px;height:102px;border-radius:50%;background:var(--green);color:#fff;text-align:center;z-index:2}
.new-order .plus{font-size:26px;font-weight:300;line-height:26px;margin-top:22px}
.new-order .lbl{font-size:13px;font-weight:300}
.tile{position:absolute;width:126px;color:#e6ebf0;text-align:center;font-size:11px;font-weight:300}
.tile small{display:block;font-size:7.5px;color:var(--green);margin-top:4px}
/* service */
.opt{position:absolute;width:40px;height:40px;border-radius:50%;border:1px solid #c9ccd0;display:flex;align-items:center;justify-content:center}
.opt.on{background:var(--green);border-color:var(--green)}
.opt-label{position:absolute;width:70px;text-align:center;font-size:10px;color:var(--ink)}
.opt-label small{display:block;font-size:7px;font-weight:500;color:var(--green);margin-top:1px}
.price{position:absolute;font-family:"Source Serif 4",serif;font-size:13px;color:var(--green)}
/* summary ticket */
.ticket{position:absolute;left:35px;top:108px;width:186px;height:220px;background:var(--navy);border-radius:3px}
.ticket::after{content:"";position:absolute;inset:4px;border:1px dashed rgba(255,255,255,.25)}
.t-row{position:absolute;left:0;width:100%;text-align:center;color:#fff}
.t-rule{position:absolute;left:18px;right:18px;height:1px;background:rgba(255,255,255,.18)}
</style>
</head>
<body>

<div class="deck-title">FoldKite | UX/UI deisgn | <b>v 3.0</b></div>

<!-- Screen 1: Log in -->
<section class="screen" style="left:141px;top:86px">
  <div class="login-bg" role="img" aria-label="Photo of young friends relaxing outdoors, tinted blue"></div>
  <div class="brand">FoldKite</div>
  <div class="abs login-copy" style="top:125px">Leave the laundry to us,<br>you go out and have some fun!</div>
  <div class="abs login-copy" style="top:197px">Username</div>
  <div class="login-field" style="top:218px"></div>
  <div class="abs" style="top:236px;color:#fff;font-size:13px;letter-spacing:1px">•••••••</div>
  <div class="login-field" style="top:256px"></div>
  <div class="login-btn">LOG IN</div>
  <div class="abs login-copy" style="top:320px">Forgot your password?</div>
  <div class="abs login-copy" style="top:405px">First time? Register</div>
</section>

<!-- Screen 2: Home -->
<section class="screen" style="left:498px;top:86px;background:var(--navy)">
  <div class="home-top"></div>
  <svg class="icon-btn" style="top:24px" width="12" height="12" viewBox="0 0 12 12"><path d="M1 1L11 11M11 1L1 11" stroke="#555" stroke-width="1.2"/></svg>
  <div class="avatar" role="img" aria-label="User profile photo"></div>
  <div class="abs greet" style="top:140px"><span class="name">Mira</span> <span style="color:#888">|</span> Any loundry to do?</div>
  <svg style="position:absolute;left:180px;top:160px" width="30" height="55" viewBox="0 0 30 55"><path d="M20 2 C30 20 28 40 6 52" fill="none" stroke="var(--green)" stroke-width="1" stroke-dasharray="3 3"/><path d="M6 52 l6 -1 M6 52 l2 -5" stroke="var(--green)" stroke-width="1"/></svg>
  <div class="new-order"><div class="plus">+</div><div class="lbl">New order</div></div>
  <div style="position:absolute;left:0;top:236px;width:100%;height:107px;background:var(--navy-light)"></div>
  <div style="position:absolute;left:126px;top:236px;width:1px;height:214px;background:rgba(0,0,0,.15)"></div>
  <div style="position:absolute;left:0;top:343px;width:100%;height:1px;background:rgba(0,0,0,.15)"></div>
  <div class="tile" style="left:0;top:274px">
    <svg width="14" height="16" viewBox="0 0 14 16" style="display:block;margin:0 auto 6px"><rect x="1.5" y="2" width="11" height="13" fill="none" stroke="#dfe6ec" stroke-width="1"/><path d="M4.5 1.5h5v2h-5z M4 7h6M4 10h6M4 13h4" stroke="#dfe6ec" stroke-width="1" fill="none"/></svg>
    My orders<small>Last order: delivery</small></div>
  <div class="tile" style="left:127px;top:274px">
    <svg width="18" height="14" viewBox="0 0 18 14" style="display:block;margin:0 auto 6px"><rect x="1" y="2" width="16" height="11" rx="1" fill="none" stroke="#dfe6ec"/><rect x="10" y="5.5" width="7" height="4" fill="none" stroke="#dfe6ec"/></svg>
    Wallet<small>+ $12.25</small></div>
  <div class="tile" style="left:0;top:384px">
    <svg width="16" height="16" viewBox="0 0 16 16" style="display:block;margin:0 auto 6px"><circle cx="8" cy="8" r="7" fill="none" stroke="#dfe6ec"/><text x="8" y="11" text-anchor="middle" font-size="8" fill="#dfe6ec" font-family="Roboto,sans-serif">$</text></svg>
    Pricing</div>
  <div class="tile" style="left:127px;top:384px">
    <svg width="16" height="16" viewBox="0 0 16 16" style="display:block;margin:0 auto 6px"><circle cx="8" cy="8" r="6" fill="none" stroke="#dfe6ec" stroke-dasharray="2.5 1.2"/><circle cx="8" cy="8" r="2.5" fill="none" stroke="#dfe6ec"/></svg>
    Settings</div>
</section>

<!-- Screen 3: Pickup -->
<section class="screen" style="left:854px;top:86px">
  <svg class="icon-btn" style="top:13px" width="12" height="12" viewBox="0 0 12 12"><path d="M1 1L11 11M11 1L1 11" stroke="#555" stroke-width="1.2"/></svg>
  <div class="abs hdr" style="top:38px"><span class="lead">New order</span> | Pickup</div>
  <svg style="position:absolute;left:38px;top:36px" width="50" height="26" viewBox="0 0 50 26"><path d="M4 24 C8 8 26 2 46 4" fill="none" stroke="var(--green)" stroke-dasharray="2 2"/></svg>
  <div class="step" style="left:34px;top:64px">1</div>
  <div class="field-label" style="top:94px">Address</div>
  <div class="rule" style="top:108px"></div>
  <div class="arrow" style="left:50px;top:119px">⌄</div>
  <div class="val" style="left:78px;top:114px;font-size:10px;line-height:12px">4120 Alder Lane<br>Maple Bend, OR 97999</div>
  <div class="rule" style="top:143px"></div>
  <div class="tag" style="left:78px;top:150px"><span style="display:inline-block;width:9px;height:9px;border:1px solid var(--green);border-radius:50%;text-align:center;line-height:7px;margin-right:3px">+</span>ADD NEW ADDRESS</div>
  <div class="field-label" style="top:174px">Date</div>
  <div class="rule" style="top:189px"></div>
  <div class="tag" style="left:78px;top:195px">SAT</div>
  <div class="arrow" style="left:50px;top:204px">‹</div>
  <div class="val" style="left:78px;top:205px">12. Mar 2016</div>
  <div class="arrow" style="left:166px;top:204px">›</div>
  <div class="rule" style="top:222px"></div>
  <div class="field-label" style="top:246px">Time</div>
  <div class="rule" style="top:260px"></div>
  <div class="tag" style="left:78px;top:266px">AM</div>
  <div class="arrow" style="left:50px;top:275px">⌄</div>
  <div class="val" style="left:78px;top:277px">11:00 to 12:00</div>
  <div class="arrow" style="left:166px;top:277px">⌃</div>
  <div class="rule" style="top:293px"></div>
  <div class="tag" style="left:98px;top:333px"><span style="display:inline-block;width:9px;height:9px;border:1px solid var(--green);border-radius:50%;margin-right:3px;vertical-align:-2px"></span>ADD NOTES</div>
  <div class="bar">NEXT</div>
</section>

<!-- Screen 4: Service -->
<section class="screen" style="left:141px;top:661px">
  <svg class="icon-btn" style="top:13px" width="8" height="13" viewBox="0 0 8 13"><path d="M7 1L1 6.5L7 12" fill="none" stroke="#555" stroke-width="1.2"/></svg>
  <div class="abs hdr" style="top:39px"><span class="lead">New order</span> | Service</div>
  <div class="step" style="left:35px;top:64px">1</div>
  <svg style="position:absolute;left:50px;top:66px" width="42" height="10" viewBox="0 0 42 10"><path d="M2 3 C14 10 28 10 40 4" fill="none" stroke="var(--green)" stroke-dasharray="2 2"/></svg>
  <div class="step" style="left:92px;top:64px">2</div>
  <div class="field-label" style="top:95px;left:35px">Service speed</div>
  <div class="rule" style="top:108px;left:35px"></div>
  <div class="opt" style="left:35px;top:122px"><svg width="14" height="18" viewBox="0 0 14 18"><circle cx="7" cy="4" r="2.5" fill="none" stroke="#aaa"/><path d="M4 9h6v8H4z" fill="none" stroke="#aaa"/></svg></div>
  <div class="opt on" style="left:106px;top:122px"><svg width="22" height="12" viewBox="0 0 22 12"><path d="M2 9V6l3-4h10l4 4v3z" fill="none" stroke="#fff"/><circle cx="6" cy="10" r="1.5" fill="#fff"/><circle cx="16" cy="10" r="1.5" fill="#fff"/></svg></div>
  <div class="opt" style="left:177px;top:122px"><svg width="12" height="18" viewBox="0 0 12 18"><path d="M6 1C9 4 9 9 8 12H4C3 9 3 4 6 1z M4 12l-2 4M8 12l2 4" fill="none" stroke="#aaa"/></svg></div>
  <div class="opt-label" style="left:20px;top:169px">Regular<small>4 DAYS</small></div>
  <div class="opt-label" style="left:91px;top:169px">Express<small>2 DAYS</small></div>
  <div class="opt-label" style="left:162px;top:169px">Cosmic<small>1 DAY</small></div>
  <div class="field-label" style="top:213px;left:35px">Service list</div>
  <div class="rule" style="top:226px;left:35px"></div>
  <div class="opt on" style="left:35px;top:236px"><svg width="20" height="16" viewBox="0 0 20 16"><path d="M10 2v12M4 4h12M4 4l-3 6h6zM16 4l-3 6h6z M6 14h8" fill="none" stroke="#fff"/></svg></div>
  <div class="opt on" style="left:106px;top:236px"><svg width="22" height="14" viewBox="0 0 22 14"><path d="M11 2a2 2 0 1 1 0 3v2L2 12h18L11 7" fill="none" stroke="#fff"/></svg></div>
  <div class="opt" style="left:177px;top:236px"><svg width="14" height="16" viewBox="0 0 14 16"><rect x="1" y="1" width="12" height="14" fill="none" stroke="#aaa"/><circle cx="7" cy="9" r="3" fill="none" stroke="#aaa"/></svg></div>
  <div class="opt-label" style="left:20px;top:283px">Kg Wash<small>4 KG</small></div>
  <div class="opt-label" style="left:91px;top:283px">Pc Wash<small>2 PCS</small></div>
  <div class="opt-label" style="left:162px;top:283px">Dry Clean<small>-</small></div>
  <div class="rule" style="top:310px;left:35px"></div>
  <div class="price" style="left:38px;top:316px">$10.00</div>
  <div class="price" style="left:110px;top:316px">$2.00</div>
  <div class="rule" style="top:337px;left:35px"></div>
  <div class="total-label" style="top:348px;right:35px">TOTAL CHARGED</div>
  <div class="total" style="top:356px;right:35px">$12.00</div>
  <div class="bar">NEXT</div>
</section>

<!-- Screen 5: Return -->
<section class="screen" style="left:503px;top:651px">
  <svg class="icon-btn" style="top:13px" width="8" height="13" viewBox="0 0 8 13"><path d="M7 1L1 6.5L7 12" fill="none" stroke="#555" stroke-width="1.2"/></svg>
  <div class="abs hdr" style="top:39px"><span class="lead">New order</span> | Return</div>
  <div class="step" style="left:35px;top:64px">1</div>
  <div class="step" style="left:93px;top:64px">2</div>
  <svg style="position:absolute;left:108px;top:66px" width="44" height="10" viewBox="0 0 44 10"><path d="M2 3 C14 10 30 10 42 4" fill="none" stroke="var(--green)" stroke-dasharray="2 2"/></svg>
  <div class="step" style="left:153px;top:64px">3</div>
  <div class="field-label" style="top:94px;left:35px">Return date</div>
  <div class="rule" style="top:108px;left:35px"></div>
  <div class="tag" style="left:78px;top:114px">SAT</div>
  <div class="arrow" style="left:52px;top:124px">‹</div>
  <div class="val" style="left:78px;top:124px">14. Mar 2016</div>
  <div class="arrow" style="left:166px;top:123px">›</div>
  <div class="rule" style="top:143px;left:35px"></div>
  <div class="field-label" style="top:167px;left:35px">Time</div>
  <div class="rule" style="top:181px;left:35px"></div>
  <div class="tag" style="left:78px;top:187px">AM</div>
  <div class="arrow" style="left:52px;top:195px">⌄</div>
  <div class="val" style="left:78px;top:196px">11:00 to 12:00</div>
  <div class="arrow" style="left:166px;top:195px">⌃</div>
  <div class="rule" style="top:214px;left:35px"></div>
  <div class="total-label" style="top:348px">TOTAL CHARGED</div>
  <div class="total" style="top:356px">$12.00</div>
  <div class="bar">NEXT</div>
</section>

<!-- Screen 6: Summary -->
<section class="screen" style="left:854px;top:651px">
  <svg class="icon-btn" style="top:13px" width="8" height="13" viewBox="0 0 8 13"><path d="M7 1L1 6.5L7 12" fill="none" stroke="#555" stroke-width="1.2"/></svg>
  <div class="abs hdr" style="top:39px"><span class="lead">New order</span> | Summary</div>
  <div class="step" style="left:35px;top:64px">1</div>
  <div class="step" style="left:92px;top:64px">2</div>
  <div class="step" style="left:154px;top:64px">3</div>
  <svg style="position:absolute;left:170px;top:58px" width="46" height="14" viewBox="0 0 46 14"><path d="M2 10 C12 0 32 0 44 10" fill="none" stroke="var(--green)" stroke-dasharray="2 2"/></svg>
  <div class="step" style="left:216px;top:64px">4</div>
  <div class="abs serif" style="top:92px;font-size:10.5px;font-weight:400">Order #7869</div>
  <div class="ticket">
    <div class="t-row" style="top:10px;font-size:10px;line-height:12.5px">4120 Alder Lane<br>Maple Bend, OR 97999</div>
    <div class="t-row" style="top:49px;font-size:7px;font-weight:500;color:var(--green)">11:00 TO 12:00</div>
    <div class="t-row" style="top:58px;font-size:11.5px">12. Mar 2016</div>
    <div class="t-rule" style="top:80px"></div>
    <div class="t-row" style="top:90px;font-size:7.5px;font-weight:500;color:var(--green)">EXPRESS SERVICE - 2 DAYS</div>
    <div class="t-rule" style="top:110px"></div>
    <div style="position:absolute;left:18px;top:122px;color:#fff;font-size:10.5px;line-height:14px;font-weight:300">4 Kg(s) Wash<br>3 Pc(s) Wash</div>
    <div class="serif" style="position:absolute;right:18px;top:122px;color:var(--green);font-size:11.5px;line-height:14px;text-align:right;font-weight:400">$10.00<br>$2.00</div>
    <div class="t-rule" style="top:160px"></div>
    <div class="t-row" style="top:173px;font-size:7px;font-weight:500;color:var(--green)">11:00 TO 12:00</div>
    <div class="t-row" style="top:182px;font-size:11.5px">14. Mar 2016</div>
    <div class="t-rule" style="top:205px"></div>
  </div>
  <div class="abs" style="top:339px;font-size:7.5px;font-weight:500">TOTAL CHARGED</div>
  <div class="abs serif" style="top:347px;font-size:23px;color:var(--green)">$12.00</div>
  <div class="bar">CONFIRM</div>
</section>

</body>
</html>
```